Rostane - telephone directory add

We need simple artwork advertisement for insertion in a local yellow pages telephone directory
Design brief for telephone ads
This project is to provide a pair of 62mm high x 91mm wide ‘yellow page adds’ for our company to place in a local phone book.
• They should reflect the same theme
• They should be based on a white ‘knock out’ background (printed on yellow paper) and have one colour in addition to black.
• Rostane is our trading name
• Main contact details are www.Rostane.example, telephone 417652, sales@rostane, social.example/rostanemotortrading
• Our address is Petites Vergees Lane, Les Corvets, GY9 7QX
• First box
o Vehicle sales – (we would like to promote)
 Japanese Minivan specialist
 European & UK vehicles supplied at best prices
 Vans and light commercials available
 Trusted supplier with 20 years experience

• Second box
o Service and repairs to all models
 Popular £99 service health check
 Qualified mechanics
 Wheel alignment & Air conditioning
 Fleet servicing options

Target Market(s)

local readers

Industry/Entity Type

Automotive

Requirements
Must have
• Design brief for telephone ads
• This project is to provide a pair of 62mm high x 91mm wide ‘yellow page adds’ for our company to place in a local phone book.
• • They should reflect the same theme
• • They should be based on a white ‘knock out’ background (printed on yellow paper) and have one colour in addition to black.
• • Rostane is our trading name
• • Main contact details are www.Rostane.example, telephone 417652, sales@rostane, social.example/rostanemotortrading
• • Our address is Petites Vergees Lane, Les Corvets, GY9 7QX
• • First box
• o Vehicle sales – (we would like to promote)
•  Japanese Minivan specialist
•  European & UK vehicles supplied at best prices
•  Vans and light commercials available
•  Trusted supplier with 20 years experience
• • Second box
• o Service and repairs to all models
•  Popular £99 service health check
•  Qualified mechanics
•  Wheel alignment & Air conditioning
•  Fleet servicing options
Nice to have
• see attached word doc
• • First box
• • Second box
•  Qualified mechanics

```html
<!DOCTYPE html>
<html lang="en">
<head>
<meta charset="utf-8">
<title>Rostane – directory adverts</title>
<link href="https://fonts.googleapis.com/css2?family=Michroma&family=Source+Sans+3:wght@400;600;800&display=swap" rel="stylesheet">
<style>
:root{
  --ink:#000;
  --paper:#fff;
  --accent:#3556d8;
  --backdrop:#e4e4e4;
}
*{box-sizing:border-box;margin:0;padding:0}
html,body{width:960px;height:1200px;overflow:hidden;background:var(--backdrop)}
body{position:relative;font-family:"Source Sans 3",sans-serif;color:var(--ink)}
.ad{position:absolute;left:186px;width:590px;height:402px;background:var(--paper)}
.ad--sales{top:150px}
.ad--service{top:670px}
.ad__header{position:absolute;top:24px;left:0;right:0;height:97px;background:var(--ink)}
.brand{position:absolute;left:32px;top:33px;display:flex;align-items:center;gap:10px}
.brand__dot{width:14px;height:14px;border-radius:50%;background:var(--accent)}
.brand__name{font-family:"Michroma",sans-serif;font-size:24px;color:var(--accent);letter-spacing:1px}
.contacts{position:absolute;right:30px;top:11px;list-style:none;text-align:right;color:var(--paper);font-size:13.5px;line-height:19px}
.contacts li{display:flex;justify-content:flex-end;align-items:center;gap:8px}
.contacts svg{width:10px;height:10px;fill:var(--paper)}
.ad__title{position:absolute;left:31px;top:142px;font-family:"Michroma",sans-serif;font-size:24px;letter-spacing:.8px;font-weight:400;line-height:30px;padding-bottom:2px;border-bottom:4px solid var(--ink);padding-right:6px;-webkit-text-stroke:.8px var(--ink)}
.features{position:absolute;left:31px;top:198px;list-style:none;font-size:23px;font-weight:600;line-height:29px}
.features li{display:flex;align-items:center;gap:10px}
.features svg{width:17px;height:17px;flex:none}
.features b{font-weight:800}
.ad__footer{position:absolute;left:0;right:0;top:341px;height:31px;background:var(--ink);color:var(--paper);font-size:14.5px;display:flex;align-items:center;padding-left:31px;gap:10px}
.ad__footer svg{width:18px;height:18px}
</style>
</head>
<body>
<svg width="0" height="0" style="position:absolute">
  <defs>
    <symbol id="tick" viewBox="0 0 20 20"><path d="M17 9.5A7.5 7.5 0 1 1 13 3" fill="none" stroke="#000" stroke-width="1.8"/><path d="M6 9.5l3.5 3.5L18 4" fill="none" stroke="#000" stroke-width="2"/></symbol>
    <symbol id="globe" viewBox="0 0 10 10"><circle cx="5" cy="5" r="4.5"/><path d="M0.5 5h9M5 .5v9" stroke="#000" stroke-width=".8"/></symbol>
    <symbol id="phone" viewBox="0 0 10 10"><path d="M1 3c0-1.5 8-1.5 8 0v1H7V3H3v1H1zM2 5h6l1 4H1z"/></symbol>
    <symbol id="mail" viewBox="0 0 10 10"><rect x="0" y="2" width="10" height="6"/><path d="M0 2l5 3.5L10 2" fill="none" stroke="#000" stroke-width=".8"/></symbol>
    <symbol id="square" viewBox="0 0 10 10"><rect x="0.5" y="0.5" width="9" height="9" rx="1.5"/></symbol>
    <symbol id="pin" viewBox="0 0 20 20"><path d="M10 2a5 5 0 0 1 5 5c0 4-5 9-5 9s-5-5-5-9a5 5 0 0 1 5-5z" fill="none" stroke="#fff" stroke-width="1.3"/><circle cx="10" cy="7" r="1.8" fill="none" stroke="#fff" stroke-width="1.2"/><ellipse cx="10" cy="17" rx="7" ry="2" fill="none" stroke="#fff" stroke-width="1.2"/></symbol>
  </defs>
</svg>

<section class="ad ad--sales">
  <header class="ad__header">
    <div class="brand"><span class="brand__dot"></span><span class="brand__name">ROSTANE</span></div>
    <ul class="contacts">
      <li>www.Rostane.example <svg><use href="#globe"/></svg></li>
      <li>417652 <svg><use href="#phone"/></svg></li>
      <li>sales@rostane <svg><use href="#mail"/></svg></li>
      <li>social.example/rostanemotortrading <svg><use href="#square"/></svg></li>
    </ul>
  </header>
  <h2 class="ad__title">Vehicle SALES</h2>
  <ul class="features">
    <li><svg><use href="#tick"/></svg>Japanese Minivan specialist</li>
    <li><svg><use href="#tick"/></svg>European &amp; UK vehicles supplied at best prices</li>
    <li><svg><use href="#tick"/></svg>Vans and light commercials available</li>
    <li><svg><use href="#tick"/></svg><span>Trusted supplier with <b>20 years experience</b></span></li>
  </ul>
  <footer class="ad__footer"><svg><use href="#pin"/></svg>Petites Vergees Lane, Les Corvets, GY9 7QX</footer>
</section>

<section class="ad ad--service">
  <header class="ad__header">
    <div class="brand"><span class="brand__dot"></span><span class="brand__name">ROSTANE</span></div>
    <ul class="contacts">
      <li>www.Rostane.example <svg><use href="#globe"/></svg></li>
      <li>417652 <svg><use href="#phone"/></svg></li>
      <li>sales@rostane <svg><use href="#mail"/></svg></li>
      <li>social.example/rostanemotortrading <svg><use href="#square"/></svg></li>
    </ul>
  </header>
  <h2 class="ad__title">Service and repairs to all models</h2>
  <ul class="features">
    <li><svg><use href="#tick"/></svg><span>Popular <b>£99</b> service health check</span></li>
    <li><svg><use href="#tick"/></svg>Qualified mechanics</li>
    <li><svg><use href="#tick"/></svg>Wheel alignment &amp; Air conditioning</li>
    <li><svg><use href="#tick"/></svg>Fleet servicing options</li>
  </ul>
  <footer class="ad__footer"><svg><use href="#pin"/></svg>Petites Vergees Lane, Les Corvets, GY9 7QX</footer>
</section>
</body>
</html>
```